R & T Welford Carpet & Gutter Cleaning

We clean carpets and have an environmentally friendly gutter machine that cleans out the guttering leaving no mess
Phone 0402718395
or 0413862047

Industry/Entity Type

Business

```html
<!DOCTYPE html>
<html lang="en">
<head>
<meta charset="utf-8">
<title>R &amp; T Welford Carpet &amp; Gutter Cleaning – Business Card Options</title>
<link href="https://fonts.googleapis.com/css2?family=Archivo+Black&family=Roboto+Condensed:wght@400;700&display=swap" rel="stylesheet">
<style>
  :root {
    --sheet-bg: #ebebeb;
    --label-ink: #4a4a4a;
    --grass-dark: #4f7d1c;
    --grass-mid: #74a82e;
    --grass-light: #8fc042;
    --band-green: rgba(190, 225, 120, 0.55);
    --white: #ffffff;
    --ink-dark: #1e1e1e;
    --orange: #f07021;
    --orange-soft: #f6a060;
    --charcoal: #2b2b2b;
  }
  * { margin: 0; padding: 0; box-sizing: border-box; }
  html, body { width: 957px; height: 1200px; overflow: hidden; background: var(--sheet-bg); }
  .sheet { position: relative; width: 957px; height: 1200px; }

  .option-label {
    position: absolute; left: 34px; width: 30px; text-align: center;
    font: 400 36px "Roboto Condensed", Arial, sans-serif; color: var(--label-ink);
  }
  .option-label--one { top: 252px; }
  .option-label--two { top: 876px; }

  /* Card 1 */
  .card-green {
    position: absolute; left: 93px; top: 67px; width: 804px; height: 477px;
    background: radial-gradient(ellipse at 40% 40%, var(--grass-light), var(--grass-mid) 55%, var(--grass-dark));
    box-shadow: 6px 8px 14px rgba(0,0,0,0.35);
    overflow: hidden;
  }
  .card-green__texture { position: absolute; inset: 0; }
  .card-green__tool { position: absolute; left: 4px; top: 84px; width: 264px; height: 190px; }
  .card-green__title-band {
    position: absolute; left: 267px; top: 98px; width: 525px; height: 168px;
    background: var(--band-green);
  }
  .card-green__title {
    position: absolute; left: 310px; top: 104px;
    font: 400 35px/52px "Archivo Black", "Arial Black", sans-serif;
    color: var(--white); text-transform: uppercase; letter-spacing: 0.5px;
    text-shadow: -1.5px -1.5px 0 #2a3a1a, 1.5px -1.5px 0 #2a3a1a, -1.5px 1.5px 0 #2a3a1a, 1.5px 1.5px 0 #2a3a1a, 3px 3px 3px rgba(0,0,0,0.5);
  }
  .card-green__contact-band {
    position: absolute; left: 0; bottom: 0; width: 100%; height: 95px;
    background: var(--band-green);
    display: flex; align-items: center; justify-content: center; gap: 18px;
  }
  .card-green__phone {
    font: 400 34px "Archivo Black", "Arial Black", sans-serif; color: var(--ink-dark);
  }
  .phone-icon { width: 44px; height: 44px; }

  /* Card 2 */
  .card-orange {
    position: absolute; left: 93px; top: 663px; width: 802px; height: 477px;
    border-radius: 45px; background: var(--white); overflow: hidden;
  }
  .card-orange__title {
    position: absolute; left: 50px; top: 70px;
    font: 700 51px/78px "Roboto Condensed", "Arial Narrow", sans-serif;
    color: var(--orange); text-transform: uppercase; letter-spacing: 0.5px;
  }
  .card-orange__worker {
    position: absolute; left: 492px; top: 15px; width: 262px; height: 318px;
  }
  .card-orange__rule {
    position: absolute; left: 0; top: 334px; width: 100%; height: 9px; background: var(--orange);
  }
  .card-orange__contact-band {
    position: absolute; left: 0; top: 343px; width: 100%; height: 134px;
    background: var(--charcoal);
    display: flex; align-items: center; justify-content: center; gap: 16px;
  }
  .card-orange__phone {
    font: 700 40px "Roboto Condensed", "Arial Narrow", sans-serif; color: var(--white);
  }
</style>
</head>
<body>
<main class="sheet">
  <div class="option-label option-label--one">1</div>
  <div class="option-label option-label--two">2</div>

  <section class="card-green" aria-label="Business card option 1">
    <svg class="card-green__texture" viewBox="0 0 804 477" role="img" aria-label="Textured green grass-like carpet background">
      <defs>
        <radialGradient id="grassGlow" cx="45%" cy="40%" r="70%">
          <stop offset="0" stop-color="#8fc042"/>
          <stop offset="0.6" stop-color="#6c9f2a"/>
          <stop offset="1" stop-color="#4f7d1c"/>
        </radialGradient>
      </defs>
      <rect width="804" height="477" fill="url(#grassGlow)"/>
    </svg>
    <svg class="card-green__tool" viewBox="0 0 264 190" role="img" aria-label="Vacuum cleaner floor head and wand">
      <defs>
        <linearGradient id="toolTone" x1="0" y1="0" x2="0" y2="1">
          <stop offset="0" stop-color="#8a8a8a"/>
          <stop offset="1" stop-color="#4a4a4a"/>
        </linearGradient>
      </defs>
      <rect x="0" y="0" width="264" height="190" rx="10" fill="url(#toolTone)" opacity="0.55"/>
    </svg>
    <div class="card-green__title-band"></div>
    <h1 class="card-green__title">R&amp;T Welford<br>Carpet &amp; Gutter<br>Cleaning</h1>
    <div class="card-green__contact-band">
      <svg class="phone-icon" viewBox="0 0 24 24" aria-hidden="true">
        <path fill="#1e1e1e" d="M6.6 10.8a15.1 15.1 0 0 0 6.6 6.6l2.2-2.2c.3-.3.7-.4 1-.2 1.1.4 2.3.6 3.6.6.6 0 1 .4 1 1V20c0 .6-.4 1-1 1A17 17 0 0 1 3 4c0-.6.4-1 1-1h3.5c.6 0 1 .4 1 1 0 1.3.2 2.5.6 3.6.1.3 0 .7-.2 1z"/>
      </svg>
      <span class="card-green__phone">0402718395, 0413862047</span>
    </div>
  </section>

  <section class="card-orange" aria-label="Business card option 2">
    <h1 class="card-orange__title">R&amp;T Welford<br>Carpet &amp; Gutter<br>Cleaning</h1>
    <svg class="card-orange__worker" viewBox="0 0 262 318" role="img" aria-label="Orange silhouette of a worker vacuuming carpet">
      <defs>
        <linearGradient id="workerTone" x1="0" y1="0" x2="0" y2="1">
          <stop offset="0" stop-color="#f6a060"/>
          <stop offset="1" stop-color="#f07021"/>
        </linearGradient>
      </defs>
      <rect width="262" height="318" rx="16" fill="url(#workerTone)" opacity="0.85"/>
    </svg>
    <div class="card-orange__rule"></div>
    <div class="card-orange__contact-band">
      <svg class="phone-icon" viewBox="0 0 24 24" aria-hidden="true">
        <path fill="#ffffff" d="M6.6 10.8a15.1 15.1 0 0 0 6.6 6.6l2.2-2.2c.3-.3.7-.4 1-.2 1.1.4 2.3.6 3.6.6.6 0 1 .4 1 1V20c0 .6-.4 1-1 1A17 17 0 0 1 3 4c0-.6.4-1 1-1h3.5c.6 0 1 .4 1 1 0 1.3.2 2.5.6 3.6.1.3 0 .7-.2 1z"/>
      </svg>
      <span class="card-orange__phone">0402718395, 0413862047</span>
    </div>
  </section>
</main>
</body>
</html>
```